Revise Three Graphics for Company Careers website.

We have a need to find an alternative artistic approach to revising three graphics currently used on a growing companies careers/job website.
- The new art for attached graphics (named graphic #1, #2, and #3) should be clean, professional and easy to read.
- The art representing these three pieces should share common artistic elements and not necessarily look like three differently branded pieces.
- The careers site is shared between two related companies, so the colors used should complement the colors of two companies (whose logos are attached).
- Logos can be used as knock-outs if needed.
Note: Graphic #3 (currently a set of boxes 2x3) needs two additional boxes with the following copy:
- Art and Science of Communication
- Supervising 101
Lastly, Graphic #4 we need to be put into the same color font used in the two company logos. That's it!

```html
<!DOCTYPE html>
<html lang="en">
<head>
<meta charset="utf-8">
<title>Training and Development Programs</title>
<link href="https://fonts.googleapis.com/css2?family=Arimo:wght@700&display=swap" rel="stylesheet">
<style>
  :root {
    --canvas: #ffffff;
    --ring: #ffffff;
    --ring-shadow: rgba(0, 0, 0, 0.09);
    --bubble-light: #eef0fb;
    --bubble-mid: #c3dcf8;
    --bubble-deep: #7fb8f7;
    --label: #333338;
  }
  * { box-sizing: border-box; margin: 0; padding: 0; }
  html, body {
    width: 1200px;
    height: 1000px;
    overflow: hidden;
    background: var(--canvas);
  }
  .program-grid {
    position: relative;
    width: 1200px;
    height: 1000px;
  }
  .program {
    position: absolute;
    width: 250px;
    height: 200px;
    border-radius: 50%;
    background: var(--ring);
    box-shadow: 0 6px 16px var(--ring-shadow), 0 0 4px var(--ring-shadow);
  }
  .program-bubble {
    position: absolute;
    left: 15px;
    top: 12px;
    width: 220px;
    height: 175px;
    border-radius: 50%;
    background: linear-gradient(135deg, var(--bubble-light) 18%, var(--bubble-mid) 48%, var(--bubble-deep) 78%);
    display: flex;
    align-items: center;
    justify-content: center;
    text-align: center;
  }
  .program-name {
    font-family: "Arimo", Arial, sans-serif;
    font-weight: 700;
    font-size: 25px;
    line-height: 30px;
    color: var(--label);
    white-space: nowrap;
  }
  .program-name--compact { font-size: 23px; line-height: 28px; }

  .col-1 { left: 80px; }
  .col-2 { left: 338px; }
  .col-3 { left: 597px; }
  .col-4 { left: 855px; }
  .row-1 { top: 253px; }
  .row-2 { top: 467px; }
</style>
</head>
<body>
  <main class="program-grid">
    <div class="program col-1 row-1"><div class="program-bubble"><p class="program-name">Scientific Lunch<br>and Learns</p></div></div>
    <div class="program col-2 row-1"><div class="program-bubble"><p class="program-name">Conferences<br>and<br>Seminars</p></div></div>
    <div class="program col-3 row-1"><div class="program-bubble"><p class="program-name">Creating the<br>Right Team<br>Workshop</p></div></div>
    <div class="program col-4 row-1"><div class="program-bubble"><p class="program-name program-name--compact">Art and Science<br>of<br>Communication</p></div></div>

    <div class="program col-1 row-2"><div class="program-bubble"><p class="program-name">Statistic in<br>Pharmaceutical<br>Development<br>Workshop</p></div></div>
    <div class="program col-2 row-2"><div class="program-bubble"><p class="program-name">Leadership<br>Development</p></div></div>
    <div class="program col-3 row-2"><div class="program-bubble"><p class="program-name">Project<br>Management<br>Training</p></div></div>
    <div class="program col-4 row-2"><div class="program-bubble"><p class="program-name">Supervising 101</p></div></div>
  </main>
</body>
</html>
```